Swim school needs flyer design

Need revamp of flyer design. Attached last years flyer (BCP A4 Holiday Leaflet-v6.2 (1)). Also attached is this years information in word format (BCP A4 BCP & Holiday Leaflet 2014-2015).
This flyer must fit with our logo (Blue Current Pools-RGB). This flyer is our first point of call for many of our clients. With the amount of information that must be provided, it is important that it flows and is appealing. Photos can be accessed from http://kemapics.brightfolio.net/apps/photos/album?albumid=52930417 or from your own source
Important that the final design fits printers template.(Flyers-A4-210x297mm-2Side - attached)

```html
<!DOCTYPE html>
<html lang="en">
<head>
<meta charset="utf-8">
<title>Holiday Swim Classes – Blue Current Pools</title>
<link rel="stylesheet" href="https://fonts.googleapis.com/css2?family=Fredoka:wght@400;500;600&family=Questrial&display=swap">
<style>
  :root {
    --blue: #10a7d9;
    --green: #b6cc2f;
    --green-dark: #1f8c3d;
    --orange: #f2931f;
    --orange-soft: #fbba6c;
    --ink: #262626;
    --white: #ffffff;
    --round: "Fredoka", sans-serif;
    --light: "Questrial", sans-serif;
  }
  * { box-sizing: border-box; margin: 0; padding: 0; }
  html, body { width: 887px; height: 1200px; overflow: hidden; background: #fff; }
  .flyer { position: relative; width: 887px; height: 1200px; overflow: hidden; font-family: var(--light); color: var(--ink); }
  .backdrop { position: absolute; inset: 0; }
  .abs { position: absolute; }

  .web { left: 52px; top: 41px; font: 500 20px var(--round); color: var(--orange); display: flex; align-items: center; gap: 7px; }
  .phone { left: 50px; top: 66px; font: 600 54px/1 var(--round); color: var(--green); display: flex; align-items: center; gap: 6px; }

  .brand { right: 50px; top: 112px; display: flex; align-items: center; gap: 10px; font: 600 35px var(--round); color: var(--blue); }
  .brand-dot { width: 22px; height: 22px; border-radius: 50%; background: var(--orange); }

  .dates { left: 26px; top: 371px; width: 373px; height: 330px; background: var(--blue); border-radius: 14px; }
  .year { position: absolute; left: 30px; font: 600 27px var(--round); color: var(--white); }
  .pill { position: absolute; left: 113px; width: 230px; height: 33px; border-radius: 17px; background: var(--white); font-size: 17px; line-height: 33px; padding-left: 27px; color: var(--ink); }
  .pill.alt { background: var(--orange-soft); }
  .note { left: 57px; top: 710px; font-size: 13.5px; }

  .locations { left: 54px; top: 750px; width: 380px; }
  .locations h2 { font: 600 20px/29px var(--round); color: var(--ink); margin-bottom: 9px; }
  .tag { display: inline-block; background: var(--green-dark); color: var(--white); font: 500 18px/23px var(--round); padding: 0 28px 0 8px; border-radius: 12px; margin-left: -8px; width: 242px; }
  .detail { font-size: 14px; line-height: 20px; margin: 6px 0 10px; }
  .detail b { font-family: var(--round); font-weight: 600; }

  .photo { left: 477px; top: 357px; width: 360px; height: 224px; border-radius: 50%; background: radial-gradient(ellipse at 55% 45%, #e9c9cf 0%, #b9d6e6 45%, #6fb2d3 100%); }

  .offer { left: 460px; top: 592px; width: 385px; text-align: center; color: var(--white); }
  .offer .facts { font: 600 21px/29px var(--round); }
  .offer .terms { font: 500 16.5px/20px var(--round); margin-top: 6px; }
  .offer .limit { font-size: 14.5px; line-height: 19px; margin-top: 10px; }

  .important { left: 498px; top: 828px; width: 360px; color: var(--white); }
  .important h3 { font: 600 20px var(--round); margin-bottom: 8px; }
  .important ul { list-style: none; }
  .important li { position: relative; padding-left: 13px; font: 500 13.5px/17px var(--round); margin-bottom: 17px; }
  .important li::before { content: ""; position: absolute; left: 0; top: 5px; width: 7px; height: 7px; border-radius: 50%; background: #9ed3ec; }

  .footer { left: 0; top: 1137px; width: 887px; text-align: center; font-size: 16.5px; line-height: 21px; color: #333; }
</style>
</head>
<body>
<main class="flyer">
  <svg class="backdrop" viewBox="0 0 887 1200" width="887" height="1200" aria-hidden="true">
    <rect width="887" height="1200" fill="#fff"/>
    <path d="M444,364 C600,340 770,300 887,232 L887,1112 L460,1112 Z" fill="var(--orange)"/>
    <path d="M0,266 C250,292 500,312 700,328 C580,348 490,360 444,364 C300,372 130,370 0,362 Z" fill="var(--green)"/>
    <path d="M0,150 C220,118 520,225 880,196 L887,196 L887,232 C720,300 420,300 0,268 Z" fill="var(--blue)"/>
    <path d="M0,733 L452,733 L460,1112 L0,1112 Z" fill="var(--green)"/>
    <path d="M0,1097 C300,1112 600,1108 887,1094 L887,1112 C600,1124 300,1122 0,1118 Z" fill="var(--blue)"/>
    <text x="52" y="218" transform="rotate(7 52 218)" font-family="Fredoka, sans-serif" font-weight="600" font-size="62" fill="#fff">Holiday Swim Classes</text>
    <text x="52" y="302" transform="rotate(6 52 302)" font-family="Fredoka, sans-serif" font-weight="600" font-size="29" fill="#262626">Holiday Program Dates</text>
  </svg>

  <div class="abs web">
    <svg width="20" height="20" viewBox="0 0 20 20" aria-hidden="true"><g fill="none" stroke="#f2931f" stroke-width="1.6"><circle cx="10" cy="10" r="8.5"/><ellipse cx="10" cy="10" rx="4" ry="8.5"/><path d="M1.5 10h17M3 5.5h14M3 14.5h14"/></g></svg>
    www.bluecurrentpools.com.au
  </div>
  <div class="abs phone">
    <svg width="40" height="40" viewBox="0 0 40 40" aria-hidden="true"><circle cx="20" cy="20" r="17" fill="none" stroke="#b6cc2f" stroke-width="3"/><path d="M13 11c2-2 4 0 5 3s-2 3-1 5 3 4 5 5 2-2 5-1 4 3 2 5c-6 4-19-10-16-17z" fill="#b6cc2f"/></svg>
    9380 2764
  </div>

  <div class="abs brand"><span class="brand-dot"></span>Blue Current Pools</div>

  <section class="abs dates">
    <div class="year" style="top:16px">2014</div>
    <div class="year" style="top:168px">2015</div>
    <div class="pill alt" style="top:17px">Sep 23rd – 27th</div>
    <div class="pill" style="top:55px">Sep 30th – Oct 4th</div>
    <div class="pill alt" style="top:93px">Jan 6th – 10th</div>
    <div class="pill" style="top:129px">Jan 13th – 17th</div>
    <div class="pill alt" style="top:166px">Jan 20th – 24th</div>
    <div class="pill" style="top:206px">Mar 30th – Apr 3rd</div>
    <div class="pill alt" style="top:245px">Apr 6th – 10th</div>
    <div class="pill" style="top:281px">Jun 29th – Jul 3rd</div>
  </section>
  <p class="abs note">* $52 per child due to 4 day week</p>

  <section class="abs locations">
    <h2>Pool Locations Contact Details<br>&amp; Office Hours</h2>
    <div class="tag">Fairview P.S. Pool</div>
    <p class="detail"><b>Location:</b> 42 Laurel Street, Fairview 3091<br><b>Phone:</b> 9380 2764<br><b>Office Hours:</b> Mon-Fri 9:00am-5.30pm,<br>&nbsp;Sat-Sun 9.15am-12.15pm</p>
    <div class="tag">Westbrook Grammar Pool</div>
    <p class="detail"><b>Location:</b> Gate 1, Marlow Street, Westbrook 3080</p>
    <div class="tag">All Correspondence</div>
    <p class="detail"><b>Post:</b> P.O. Box 4187, East Westbrook 3080<br><b>Email:</b> info@bluecurrentpools.com.au<br><b>ABN:</b> 61 208 317 594</p>
  </section>

  <div class="abs photo" role="img" aria-label="Photo of a young swimmer in cap and goggles holding a kickboard underwater"></div>

  <section class="abs offer">
    <p class="facts">Salt Water Pool<br>Ages 3 and older<br>$75 per child per week<br>(5x½ hour classes per week)</p>
    <p class="terms">No bookings are taken without a fully completed enrolment form and payment.</p>
    <p class="limit">Places are limited so book early<br>to avoid disappointment.</p>
  </section>

  <section class="abs important">
    <h3>Important</h3>
    <ul>
      <li>All holiday swim classes are conducted at the Fairview primary school pool</li>
      <li>30 minute classes run every ½ hour from 9.30am to 12 noon</li>
      <li>Limited places due to small class sizes</li>
      <li>Beginners to advanced swimmers welcome</li>
      <li>All children are grouped by age and ability</li>
      <li>No refunds or makeups for holiday programs</li>
    </ul>
  </section>

  <p class="abs footer">Our qualified staff makes learning to swim not only a rewarding but also a lot of fun.<br>This is a great opportunity to kick-start your child’s aquatic education.</p>
</main>
</body>
</html>
```